Redesign business cards

We have a new logo and I am not that happy with the layout of our existing card and looking for a change. Font is a bit small and the green can be hard to read. Logo may need a tidy up as the copy I have is not that hi-res too so require you to produce a hi-res version of the logo for us too. There will be three individual business cards to produce with just the names and phone numbers being different. Address will change too, but use what you see on the card for now.

Industry/Entity Type

Business

Requirements
Nice to have
• You could consider a redesign to the new logo, just not too radical. We like the blue and green hexagons as we feel that they are representative of oil industry that we are in.

```html
<!DOCTYPE html>
<html lang="en">
<head>
<meta charset="utf-8">
<title>Verdex Oil Services – Business Card</title>
<link rel="stylesheet" href="https://fonts.googleapis.com/css2?family=Open+Sans:wght@400;600;700&display=swap">
<style>
  :root {
    --bg: #e9e6e1;
    --card-black: #141414;
    --card-charcoal: #222324;
    --lime: #9ccd45;
    --lime-bright: #b4e05a;
    --ink-dark: #1b1b1b;
    --ink-light: #d6d6d6;
    --white: #ffffff;
  }
  * { box-sizing: border-box; margin: 0; padding: 0; }
  html, body {
    width: 1200px; height: 1023px; overflow: hidden;
    background: var(--bg);
    font-family: "Open Sans", Arial, sans-serif;
  }
  .sheet {
    width: 1200px; height: 1023px;
    display: flex; align-items: center; justify-content: center; gap: 40px;
  }
  .card {
    position: relative;
    width: 540px; height: 309px;
    border-radius: 4px;
    overflow: hidden;
    box-shadow: 0 10px 30px rgba(0,0,0,.25);
  }

  /* Front */
  .card-front {
    background: linear-gradient(160deg, var(--card-charcoal) 0%, var(--card-black) 70%);
  }
  .brand {
    position: absolute; right: 40px; top: 44px;
    display: flex; align-items: center; gap: 12px;
  }
  .brand-mark {
    width: 22px; height: 22px; border-radius: 50%;
    background: var(--lime);
  }
  .brand-name {
    font-weight: 700; font-size: 34px; line-height: 1;
    color: var(--lime);
  }
  .brand-sub {
    position: absolute; right: 40px; top: 84px;
    font-weight: 700; font-size: 14px; color: var(--lime);
  }
  .info-band {
    position: absolute; left: 0; right: 0; bottom: 0; height: 150px;
    background: linear-gradient(90deg, var(--card-black) 0%, var(--card-black) 42%, #5d7d2a 62%, var(--lime) 85%, var(--lime-bright) 100%);
    border-top: 2px solid var(--lime);
  }
  .person {
    position: absolute; left: 32px; top: 22px;
    display: flex; align-items: baseline; gap: 8px;
  }
  .person-name {
    font-weight: 600; font-size: 20px; letter-spacing: .5px;
    text-transform: uppercase; color: var(--lime);
  }
  .person-divider { color: var(--lime); font-size: 20px; }
  .person-title { font-size: 14px; color: var(--lime); }
  .contact-list {
    position: absolute; left: 32px; top: 62px;
    list-style: none;
  }
  .contact-item {
    display: flex; align-items: center; gap: 10px;
    font-size: 14px; line-height: 22px; color: var(--ink-light);
  }
  .contact-item svg { width: 13px; height: 13px; flex: none; }
  .address {
    position: absolute; right: 36px; top: 22px;
    font-style: normal; font-size: 14px; line-height: 22px;
    color: var(--ink-dark); text-align: left;
  }

  /* Back */
  .card-back {
    background: var(--card-black);
  }
  .back-texture {
    position: absolute; inset: 0;
    background: radial-gradient(ellipse at 40% 35%, #3a3a3a 0%, #1e1e1e 55%, #121212 100%);
  }
  .back-brand {
    position: absolute; inset: 0;
    display: flex; flex-direction: column; align-items: center; justify-content: center;
  }
  .back-name {
    font-weight: 700; font-size: 76px; line-height: 1; color: var(--white);
  }
  .back-sub {
    margin-top: 8px;
    font-weight: 700; font-size: 20px; color: var(--white);
  }
</style>
</head>
<body>
<main class="sheet">

  <section class="card card-front" aria-label="Business card front">
    <div class="brand">
      <span class="brand-mark"></span>
      <span class="brand-name">Verdex</span>
    </div>
    <div class="brand-sub">Oil Services</div>

    <div class="info-band">
      <div class="person">
        <span class="person-name">Sam Porter</span>
        <span class="person-divider">|</span>
        <span class="person-title">Sales Engineer</span>
      </div>
      <ul class="contact-list">
        <li class="contact-item">
          <svg viewBox="0 0 16 16" aria-hidden="true"><path fill="#d6d6d6" d="M4 1l3 3-2 2c1 2 3 4 5 5l2-2 3 3-2 3C7 15 1 9 1 3z"/></svg>
          0412 555 018
        </li>
        <li class="contact-item">
          <svg viewBox="0 0 16 16" aria-hidden="true"><rect x="1" y="3" width="14" height="10" rx="1" fill="none" stroke="#d6d6d6" stroke-width="1.6"/><path d="M1 4l7 5 7-5" fill="none" stroke="#d6d6d6" stroke-width="1.6"/></svg>
          sam@verdex.com.au
        </li>
        <li class="contact-item">
          <svg viewBox="0 0 16 16" aria-hidden="true"><circle cx="8" cy="8" r="6.5" fill="none" stroke="#d6d6d6" stroke-width="1.5"/><path d="M1.5 8h13M8 1.5c-3 3.5-3 9.5 0 13M8 1.5c3 3.5 3 9.5 0 13" fill="none" stroke="#d6d6d6" stroke-width="1.2"/></svg>
          www.verdex.com.au
        </li>
      </ul>
      <address class="address">
        48 Harbour Street<br>
        PO Box 3150<br>
        Eastfield, Brisbane QLD 4120
      </address>
    </div>
  </section>

  <section class="card card-back" aria-label="Business card back">
    <div class="back-texture" role="img" aria-label="Dark hexagon pattern texture"></div>
    <div class="back-brand">
      <span class="back-name">Verdex</span>
      <span class="back-sub">Oil Services</span>
    </div>
  </section>

</main>
</body>
</html>
```